Baby Boutique Needs a Business Card Design

We need a modern double sided business card design using the attached logo for L' Tot Nook.

L' Tot Nook is a baby boutique which sells only handmade clothing and accessories for both boys and girls. Our store will live exclusively online.

We would like to only use the colors that have been used in the logo.

Target Market(s)

Potential wholesale clients, Small business owners

Industry/Entity Type

Retail

Contact Information for Business Card

Name Wendell R. Fauste (Owner)
Email sales@ltotnook.example
Main Phone 555-013-2947
Cell phone 555-013-6152
Website www.LTotNook.example

Font styles to use
Sans Serif

Colors

Designer to choose colors to be used in the design.

Requirements
Must have
• -Would like to have icons that indentify the contact information.
• -Include our website
• -Include our tagline in a small area near the bottom. "Handmade Baby Creations"
• -Would like to include Facebook and Instagram Icons
• -
Nice to have
• Would like to have a simple back side with the logo.
• Something along the lines of the marlow ridge card attached.

```html
<!DOCTYPE html>
<html lang="en">
<head>
<meta charset="utf-8">
<title>L' Tot Nook — Business Card</title>
<link rel="stylesheet" href="https://fonts.googleapis.com/css2?family=Arimo:wght@400;700&display=swap">
<style>
  :root {
    --page: #3a3a3c;
    --card: #202427;
    --teal: #79cbbd;
    --coral: #e56a67;
    --ink: #1d2124;
    --light: #d9dddf;
  }
  * { box-sizing: border-box; margin: 0; padding: 0; }
  html, body {
    width: 1200px; height: 1189px; overflow: hidden;
    background: var(--page);
    font-family: "Arimo", Arial, sans-serif;
  }
  .stage {
    width: 1200px; height: 1189px;
    display: flex; flex-direction: column; align-items: center; justify-content: center;
    gap: 70px;
  }
  .card {
    position: relative;
    width: 880px; height: 503px;
    background: var(--card);
    border-radius: 34px;
    overflow: hidden;
  }
  .wordmark {
    display: flex; align-items: center; gap: 18px;
    color: var(--teal);
    font-weight: 700;
    white-space: nowrap;
  }
  .wordmark-dot {
    flex: none;
    border-radius: 50%;
    background: var(--coral);
  }
  /* Front */
  .card-front .wordmark {
    position: absolute; left: 250px; top: 150px;
    font-size: 72px;
  }
  .card-front .wordmark-dot { width: 30px; height: 30px; }
  .front-band {
    position: absolute; left: 0; bottom: 58px;
    width: 760px; height: 48px;
    background: var(--teal);
    display: flex; align-items: center; justify-content: center;
    color: var(--ink);
    font-size: 24px; letter-spacing: 4px;
  }
  .social {
    position: absolute; bottom: 112px; right: 70px;
    display: flex; gap: 12px;
  }
  .social-square {
    width: 38px; height: 38px;
    background: var(--coral);
    border-radius: 3px;
  }
  /* Back */
  .card-back .wordmark {
    position: absolute; left: 70px; top: 170px;
    font-size: 56px;
  }
  .card-back .wordmark-dot { width: 24px; height: 24px; }
  .divider {
    position: absolute; left: 450px; top: 105px;
    width: 2px; height: 190px;
    background: var(--teal);
  }
  .contact {
    position: absolute; left: 500px; top: 110px;
    color: var(--light);
  }
  .contact-name {
    color: var(--teal);
    font-size: 27px; font-weight: 700;
  }
  .contact-role {
    color: var(--coral);
    font-size: 21px;
    margin-bottom: 16px;
  }
  .contact-list { list-style: none; }
  .contact-list li {
    display: flex; align-items: center; gap: 14px;
    font-size: 22px; line-height: 32px;
  }
  .contact-list svg { width: 20px; height: 20px; flex: none; }
  .back-rule {
    position: absolute; left: 0; right: 0; bottom: 108px;
    height: 5px; background: var(--coral);
  }
  .back-band {
    position: absolute; left: 0; right: 0; bottom: 56px;
    height: 48px;
    background: var(--teal);
    display: flex; align-items: center; justify-content: center;
    color: var(--ink);
    font-size: 25px; letter-spacing: 7px;
  }
</style>
</head>
<body>
<main class="stage">
  <section class="card card-front" aria-label="Card front">
    <div class="wordmark"><span class="wordmark-dot"></span>L' Tot Nook</div>
    <div class="social" aria-label="Social profiles">
      <span class="social-square"></span>
      <span class="social-square"></span>
    </div>
    <div class="front-band">www.LTotNook.example</div>
  </section>

  <section class="card card-back" aria-label="Card back">
    <div class="wordmark"><span class="wordmark-dot"></span>L' Tot Nook</div>
    <div class="divider"></div>
    <div class="contact">
      <p class="contact-name">Wendell R. Fauste</p>
      <p class="contact-role">Owner</p>
      <ul class="contact-list">
        <li>
          <svg viewBox="0 0 20 20" aria-hidden="true"><path fill="#e56a67" d="M3 7c0-3 3-4 7-4s7 1 7 4l-3 1-1-2H7L6 8 3 7zm3 3h8l2 7H4l2-7zm4 1.5a2 2 0 1 0 0 4 2 2 0 0 0 0-4z"/></svg>
          555-013-2947
        </li>
        <li>
          <svg viewBox="0 0 20 20" aria-hidden="true"><rect x="5" y="2" width="10" height="16" rx="1.5" fill="none" stroke="#e56a67" stroke-width="2"/></svg>
          555-013-6152
        </li>
        <li>
          <svg viewBox="0 0 20 20" aria-hidden="true"><rect x="2" y="4" width="16" height="12" fill="#e56a67"/><path d="M2 4l8 7 8-7M2 16l6-6M18 16l-6-6" fill="none" stroke="#202427" stroke-width="1.5"/></svg>
          sales@ltotnook.example
        </li>
        <li>
          <svg viewBox="0 0 20 20" aria-hidden="true"><circle cx="10" cy="10" r="8" fill="none" stroke="#e56a67" stroke-width="2"/><path d="M2 10h16M10 2c-4 4-4 12 0 16M10 2c4 4 4 12 0 16" fill="none" stroke="#e56a67" stroke-width="1.5"/></svg>
          www.LTotNook.example
        </li>
      </ul>
    </div>
    <div class="back-rule"></div>
    <div class="back-band">Handmade Baby Creations</div>
  </section>
</main>
</body>
</html>
```